New Letterhead Design Project

i need a logo letterhead & compliment slips for my new company the name of the company is called Harwick Civil Engineers Ltd the work we do is foundations floor slabs drainage retaining walls block paving & tarmac

Industry/Entity Type

It Company

```html
<!DOCTYPE html>
<html lang="en">
<head>
<meta charset="utf-8">
<title>Harwick Civil Engineers Ltd – Stationery</title>
<link rel="stylesheet" href="https://fonts.googleapis.com/css2?family=Cinzel:wght@500&family=Open+Sans:wght@400;600&family=Great+Vibes&display=swap">
<style>
  :root {
    --canvas: #e9e9e9;
    --paper: #ffffff;
    --paper-warm: #ecebe5;
    --ink: #2b2b2b;
    --ink-soft: #5a5a5a;
    --band: #1f1f1f;
    --band-text: #f2f2f2;
    --mark-faint: #dcdcd6;
    --rule: #3a3a3a;
  }
  * { box-sizing: border-box; margin: 0; padding: 0; }
  html, body { width: 1200px; height: 795px; overflow: hidden; }
  body {
    background: var(--canvas);
    font-family: "Open Sans", Arial, sans-serif;
    color: var(--ink);
    position: relative;
  }

  /* Letterhead */
  .letterhead {
    position: absolute;
    left: 640px; top: 30px;
    width: 520px; height: 735px;
    background: var(--paper-warm);
    box-shadow: 0 4px 14px rgba(0,0,0,.18);
    overflow: hidden;
  }
  .letterhead .faint-square {
    position: absolute;
    right: 60px; top: 200px;
    width: 300px; height: 300px;
    border: 26px solid var(--mark-faint);
    opacity: .7;
  }
  .brand {
    display: flex; align-items: center; gap: 10px;
    font-family: "Cinzel", Georgia, serif;
    font-weight: 500;
    color: var(--ink);
    letter-spacing: .5px;
  }
  .brand-square {
    width: 18px; height: 18px;
    border: 2px solid var(--ink);
  }
  .letterhead .brand {
    position: absolute; top: 48px; left: 0; right: 0;
    justify-content: center; font-size: 19px;
  }
  .letter-body {
    position: absolute; left: 50px; right: 50px; top: 120px;
    font-size: 9.5px; line-height: 1.6; color: var(--ink-soft);
  }
  .letter-body .salutation { margin-bottom: 12px; color: var(--ink); }
  .letter-body p { margin-bottom: 12px; text-align: justify; }
  .signature {
    position: absolute; left: 50px; top: 520px;
  }
  .signature .name {
    font-family: "Great Vibes", cursive;
    font-size: 30px; color: var(--ink);
  }
  .signature .role { font-size: 9px; color: var(--ink-soft); }
  .contact-band {
    position: absolute; left: 0; right: 0; bottom: 0;
    height: 56px; background: var(--band);
    color: var(--band-text);
    font-size: 9px;
    padding: 12px 34px;
    display: flex; flex-direction: column; gap: 6px;
  }
  .contact-band .row { display: flex; gap: 22px; }
  .contact-band b { font-weight: 600; }

  /* Compliment slip */
  .compliment-slip {
    position: absolute;
    left: 60px; top: 300px;
    width: 520px; height: 245px;
    background: var(--paper);
    box-shadow: 0 4px 14px rgba(0,0,0,.18);
    overflow: hidden;
  }
  .compliment-slip .brand {
    position: absolute; left: 26px; top: 26px; font-size: 17px;
  }
  .slip-contacts {
    position: absolute; left: 26px; top: 78px;
    font-size: 9px; color: var(--ink-soft);
    list-style: none;
  }
  .slip-contacts li { display: flex; align-items: center; gap: 6px; margin-bottom: 5px; }
  .slip-contacts svg { width: 10px; height: 10px; }
  .slip-contacts .address { margin-top: 4px; }
  .slip-rule {
    position: absolute; left: 26px; top: 170px;
    width: 200px; border-top: 1px solid var(--rule);
  }
  .greeting {
    position: absolute; right: 28px; top: 70px;
    font-family: "Great Vibes", cursive;
    font-size: 38px; color: var(--ink);
  }
  .compliment-slip .faint-square {
    position: absolute; right: 60px; bottom: -40px;
    width: 150px; height: 150px;
    border: 16px solid var(--mark-faint);
    opacity: .6;
  }
</style>
</head>
<body>

<section class="compliment-slip">
  <div class="faint-square"></div>
  <div class="brand"><span class="brand-square"></span>Harwick Civil Engineers Ltd</div>
  <ul class="slip-contacts">
    <li>
      <svg viewBox="0 0 10 10"><circle cx="5" cy="5" r="4.5" fill="none" stroke="#5a5a5a"/><path d="M3.3 2.8l1 1-.5.6a3 3 0 0 0 1.6 1.6l.6-.5 1 1-.7.7C4.8 7 3 5.2 2.6 3.5z" fill="#5a5a5a"/></svg>
      01632 960220
    </li>
    <li>
      <svg viewBox="0 0 10 10"><circle cx="5" cy="5" r="4.5" fill="none" stroke="#5a5a5a"/><rect x="3.5" y="2.3" width="3" height="5.4" rx=".5" fill="#5a5a5a"/></svg>
      07700 900131
    </li>
    <li>
      <svg viewBox="0 0 10 10"><circle cx="5" cy="5" r="4.5" fill="none" stroke="#5a5a5a"/><rect x="2.6" y="3.3" width="4.8" height="3.4" fill="none" stroke="#5a5a5a" stroke-width=".8"/><path d="M2.6 3.3L5 5.2l2.4-1.9" fill="none" stroke="#5a5a5a" stroke-width=".8"/></svg>
      harwickcivil@example.co.uk
    </li>
    <li class="address">14 Mill Lane, Thornbury, Ashford AB12 3CD</li>
  </ul>
  <div class="slip-rule"></div>
  <div class="greeting">With Compliments</div>
</section>

<section class="letterhead">
  <div class="faint-square"></div>
  <div class="brand"><span class="brand-square"></span>Harwick Civil Engineers Ltd</div>
  <div class="letter-body">
    <p class="salutation">Dear Client</p>
    <p>Thank you for considering us for your next groundwork project. We build foundations, floor slabs, drainage and retaining walls with care, on time and to budget, across the region and beyond.</p>
    <p>Our team also lays block paving and tarmac for homes, schools and commercial sites. Every job is planned in detail, checked at each stage and finished to a high standard that lasts for years.</p>
    <p>Please contact us to arrange a site visit and a free quotation. We look forward to working with you.</p>
  </div>
  <div class="signature">
    <div class="name">Your Name</div>
    <div class="role">Managing Director</div>
  </div>
  <footer class="contact-band">
    <div class="row">
      <span><b>Tel:</b> 01632 960220</span>
      <span><b>Mobile:</b> 07700 900131</span>
      <span><b>Email:</b> harwickcivil@example.co.uk</span>
    </div>
    <div class="row"><span>14 Mill Lane, Thornbury, Ashford AB12 3CD</span></div>
  </footer>
</section>

</body>
</html>
```